tuGlide Landing Page 2

Edit the attached page to make it more visually appealing and professional. This page is a landing page that will direct our viewers to our raisewick page. The join buttons definitely need to be changed, as well as fonts for the whole page. Please put raisewick logo on the "join us" button, and put chatterleaf and peeplark with logos on the bottom center. If there are any further questions please ask us. http://tuglide.pardovant.example/hands.html

Target Market(s)

Middle class Americans ages 20-35.

Industry/Entity Type

It Professional

```html
<!DOCTYPE html>
<html lang="en">
<head>
<meta charset="utf-8">
<title>tuGlide</title>
<link rel="stylesheet" href="https://fonts.googleapis.com/css2?family=Source+Sans+3:wght@400;600;700&display=swap">
<style>
  :root {
    --header-bg-top: #fafafa;
    --header-bg-bottom: #ececec;
    --header-edge: #cfcfcf;
    --logo-ink: #3d3d3d;
    --hero-dark: #1d1511;
    --hero-mid: #3a2d25;
    --accent-yellow: #f6b900;
    --text-white: #ffffff;
    --btn-top: #ffd25a;
    --btn-bottom: #f79b14;
    --btn-edge: #b35a00;
    --btn-ink: #6a2e00;
    --video-light: #8a8a8a;
    --video-dark: #3c3c3c;
    --footer-top: #34343d;
    --footer-bottom: #24242b;
    --footer-divider: #15151a;
    --base-bg: #161616;
    --stripe-red: #b3262b;
    --stripe-blue: #3f8fd6;
  }
  * { margin: 0; padding: 0; box-sizing: border-box; }
  html, body { width: 1200px; height: 769px; overflow: hidden; background: var(--base-bg); }
  body { position: relative; font-family: "Source Sans 3", "Myriad Pro", sans-serif; }

  .site-header {
    position: absolute; left: 0; top: 0; width: 1200px; height: 68px;
    background: linear-gradient(var(--header-bg-top), var(--header-bg-bottom));
    border-bottom: 2px solid var(--header-edge);
  }
  .brand {
    position: absolute; left: 64px; top: 8px;
    font-weight: 700; font-size: 44px; line-height: 50px; color: var(--logo-ink);
  }

  .hero {
    position: absolute; left: 0; top: 68px; width: 1200px; height: 610px;
    background: radial-gradient(ellipse at 55% 45%, var(--hero-mid), var(--hero-dark) 75%);
  }
  .hero-title { position: absolute; left: 64px; top: 116px; color: var(--accent-yellow); text-shadow: 0 2px 3px rgba(0,0,0,.6); }
  .hero-title .lead { display: block; font-size: 51px; font-weight: 600; line-height: 54px; }
  .hero-title .big { display: block; font-size: 88px; font-weight: 700; line-height: 78px; letter-spacing: -1px; }
  .hero-copy {
    position: absolute; left: 64px; top: 282px;
    font-size: 34px; line-height: 41px; color: var(--text-white);
    text-shadow: 0 1px 2px rgba(0,0,0,.6);
  }
  .join-button {
    position: absolute; left: 65px; top: 402px; width: 223px; height: 66px;
    border-radius: 7px; border-bottom: 4px solid var(--btn-edge);
    background: linear-gradient(var(--btn-top), var(--btn-bottom));
    display: flex; align-items: center; padding-left: 16px; gap: 14px;
    color: var(--btn-ink); font-size: 35px; font-weight: 600; text-decoration: none;
    box-shadow: 0 3px 6px rgba(0,0,0,.5);
  }
  .join-button .mark { width: 28px; height: 28px; border-radius: 50%; background: var(--btn-ink); }

  .video-card {
    position: absolute; left: 653px; top: 126px; width: 453px; height: 285px;
    border: 5px solid var(--text-white);
    background: radial-gradient(ellipse at 60% 50%, var(--video-light), var(--video-dark) 80%);
    display: flex; align-items: center; justify-content: center; gap: 16px;
    color: var(--text-white); font-size: 34px; font-weight: 700;
  }

  .stripe { position: absolute; left: 0; top: 678px; width: 1200px; height: 3px;
    background: linear-gradient(90deg, var(--stripe-red) 0 20px, var(--stripe-blue) 20px 180px, var(--stripe-red) 180px 330px, var(--stripe-blue) 330px 470px, var(--stripe-red) 470px 590px, var(--stripe-blue) 590px 1200px); }
  .site-footer {
    position: absolute; left: 0; top: 681px; width: 1200px; height: 60px;
    background: linear-gradient(var(--footer-top), var(--footer-bottom));
  }
  .social-nav { position: absolute; right: 50px; top: 0; height: 60px; display: flex; }
  .social-link {
    height: 60px; display: flex; align-items: center; gap: 10px; padding: 0 18px;
    color: var(--text-white); font-size: 22px; font-weight: 600; text-decoration: none;
  }
  .social-link + .social-link { border-left: 1px solid var(--footer-divider); }
  .social-link .dot { width: 20px; height: 20px; border-radius: 50%; background: var(--text-white); }
</style>
</head>
<body>
  <header class="site-header">
    <div class="brand">tuGlide</div>
  </header>

  <section class="hero" role="img" aria-label="Dark brown close-up photograph of weathered hands clasped together">
    <h1 class="hero-title"><span class="lead">You are the change</span><span class="big">you seek.</span></h1>
    <p class="hero-copy">Protecting your family and<br>your future requires your action.</p>
    <a class="join-button" href="#"><span>Join Now</span><span class="mark"></span></a>
    <div class="video-card" role="img" aria-label="Black and white photograph of two worn hands touching">
      <svg width="40" height="40" viewBox="0 0 40 40"><circle cx="20" cy="20" r="17.5" fill="none" stroke="#fff" stroke-width="3"/><path d="M16 12 L28 20 L16 28 Z" fill="#fff"/></svg>
      <span>Watch video</span>
    </div>
  </section>

  <div class="stripe"></div>
  <footer class="site-footer">
    <nav class="social-nav">
      <a class="social-link" href="#"><span class="dot"></span>Chatterleaf</a>
      <a class="social-link" href="#"><span class="dot"></span>Raisewick</a>
      <a class="social-link" href="#"><span class="dot"></span>Peeplark</a>
    </nav>
  </footer>
</body>
</html>
```